Business cards for Harbourline Supply Pty Ltd that import building products into Australia from China
Target Market(s)
Business to Business
Industry/Entity Type
Business
Contact Information for Business Card
Front: Logo and Business Name
Rear:
Vernon Ashcombe
General Manager
Mobile: 0427 619 354
email: vern@harbourlinesupply.com.au
alternative email: vern@coastwardgoods.com.au
web: www.harbourlinesupply.com.au
Adelaide, Brisbane and Darwin
Colors
ec1f27
fbee3d

```html
<!DOCTYPE html>
<html lang="en">
<head>
<meta charset="utf-8">
<title>Harbourline Supply Pty Ltd – Business Cards</title>
<link rel="stylesheet" href="https://fonts.googleapis.com/css2?family=Lato:wght@400;700;900&display=swap">
<style>
  :root {
    --brand-red: #ec1f27;
    --brand-yellow: #fbee3d;
    --ink: #2b2b2b;
    --paper: #ffffff;
    --backdrop: #3a3a3c;
  }
  * { box-sizing: border-box; margin: 0; padding: 0; }
  html, body { width: 1200px; height: 900px; overflow: hidden; }
  body {
    background: var(--backdrop);
    font-family: "Lato", sans-serif;
    position: relative;
  }
  .card {
    position: absolute;
    width: 560px;
    height: 320px;
    overflow: hidden;
    box-shadow: 0 10px 24px rgba(0,0,0,0.45);
  }
  /* Front */
  .card--front {
    left: 590px; top: 110px;
    background: var(--brand-red);
    color: var(--paper);
  }
  .front-brand {
    position: absolute;
    left: 0; right: 0; top: 88px;
    display: flex; align-items: center; justify-content: center; gap: 18px;
  }
  .brand-dot {
    width: 70px; height: 70px; border-radius: 50%;
    background: var(--brand-yellow);
    flex: none;
  }
  .brand-name {
    font-weight: 900;
    text-transform: uppercase;
    line-height: 1.02;
    letter-spacing: 0.5px;
  }
  .card--front .brand-name { font-size: 34px; color: var(--paper); }
  .front-web {
    position: absolute; left: 0; right: 0; top: 232px;
    text-align: center; font-size: 17px; letter-spacing: 1px;
  }
  /* Back */
  .card--back {
    left: 70px; top: 470px;
    background: var(--paper);
    color: var(--ink);
  }
  .back-sweep { position: absolute; inset: 0; }
  .back-brand {
    position: absolute; left: 28px; top: 26px;
    display: flex; align-items: center; gap: 12px;
  }
  .card--back .brand-dot { width: 46px; height: 46px; background: var(--brand-red); }
  .card--back .brand-name { font-size: 22px; color: var(--brand-red); }
  .holder {
    position: absolute; left: 30px; top: 116px;
  }
  .holder-name { color: var(--brand-red); font-weight: 700; font-size: 24px; }
  .holder-role { font-size: 15px; margin-top: 2px; }
  .holder-address { font-size: 15px; line-height: 1.35; margin-top: 16px; }
  .contact-list {
    position: absolute; left: 236px; top: 212px;
    list-style: none; font-size: 15px; line-height: 1.5;
  }
  .contact-list li { display: flex; align-items: center; gap: 9px; }
  .contact-icon { width: 14px; height: 14px; flex: none; }
</style>
</head>
<body>

<section class="card card--front" aria-label="Business card front">
  <div class="front-brand">
    <span class="brand-dot"></span>
    <span class="brand-name">Harbourline Supply<br>Pty Ltd</span>
  </div>
  <p class="front-web">www.harbourlinesupply.com.au</p>
</section>

<section class="card card--back" aria-label="Business card back">
  <svg class="back-sweep" width="560" height="320" viewBox="0 0 560 320" aria-hidden="true">
    <path d="M262 0 C420 20 520 150 540 320 L560 320 L560 0 Z" fill="var(--brand-yellow)"/>
    <path d="M288 0 C438 22 532 140 556 300 L560 300 L560 0 Z" fill="var(--paper)"/>
    <path d="M298 0 C442 22 536 132 560 272 L560 0 Z" fill="var(--brand-red)"/>
  </svg>

  <div class="back-brand">
    <span class="brand-dot"></span>
    <span class="brand-name">Harbourline Supply<br>Pty Ltd</span>
  </div>

  <div class="holder">
    <p class="holder-name">Vernon Ashcombe</p>
    <p class="holder-role">General Manager</p>
    <p class="holder-address">4100 Kell Road<br>Tarrow NT 0800</p>
  </div>

  <ul class="contact-list">
    <li>
      <svg class="contact-icon" viewBox="0 0 14 14" aria-hidden="true"><rect x="3.5" y="0.5" width="7" height="13" rx="1.5" fill="none" stroke="var(--brand-red)" stroke-width="1.4"/><circle cx="7" cy="11" r="0.9" fill="var(--brand-red)"/></svg>
      0427 619 354
    </li>
    <li>
      <svg class="contact-icon" viewBox="0 0 14 14" aria-hidden="true"><rect x="0.5" y="2.5" width="13" height="9" fill="var(--brand-red)"/><path d="M0.5 2.5 L7 8 L13.5 2.5" fill="none" stroke="#fff" stroke-width="1.2"/></svg>
      vern@harbourlinesupply.com.au
    </li>
    <li>
      <svg class="contact-icon" viewBox="0 0 14 14" aria-hidden="true"><rect x="0.5" y="2.5" width="13" height="9" fill="var(--brand-red)"/><path d="M0.5 2.5 L7 8 L13.5 2.5" fill="none" stroke="#fff" stroke-width="1.2"/></svg>
      vern@coastwardgoods.com.au
    </li>
    <li>
      <svg class="contact-icon" viewBox="0 0 14 14" aria-hidden="true"><circle cx="7" cy="7" r="6.2" fill="none" stroke="var(--brand-red)" stroke-width="1.3"/><ellipse cx="7" cy="7" rx="2.6" ry="6.2" fill="none" stroke="var(--brand-red)" stroke-width="1.1"/><path d="M1 7 H13" stroke="var(--brand-red)" stroke-width="1.1"/></svg>
      www.harbourlinesupply.com.au
    </li>
  </ul>
</section>

</body>
</html>
```